Letterhead Design Project

Looking for letterhead designs for Dravesco Mining.

I am looking for a letterhead design in conjunction with a business card design. I have opened contests for both but ask that if you submit a letterhead design you also submit a business card design with a corresponding look/feel.

Dravesco Mining is a B2B company that buys and sells large machinery tires within the coal mining industry. The design should the strong, crisp and masculine. I have uploaded the company logo and mock-up of the back of the company's business card.

Color scheme should be grey/green/black

Contact information to include:
Name: Tom Sealbrook
Title: Managing Director
Phone: 555-314-2097
Address: 1186 Pelham #3 Dallas, TX 75209
Email: Tom@Dravesco.example

Project Deadline Extended
Reason: Looking for a more refined, elegant letterhead than what's been submitted as of yet. Here is a sample of what we're looking for: http://www.plumbridgestudio.example/letterhead-designs/ We will also be increasing the payment.

```html
<!DOCTYPE html>
<html lang="en">
<head>
<meta charset="utf-8">
<title>Dravesco Mining Letterhead</title>
<link rel="stylesheet" href="https://fonts.googleapis.com/css2?family=Arimo:wght@700&display=swap">
<style>
  :root {
    --paper: #ffffff;
    --green: #6ab344;
    --green-soft: rgba(106, 179, 68, 0.14);
    --grey: #8c8c8c;
    --charcoal: #58595b;
  }
  html, body {
    margin: 0;
    padding: 0;
    overflow: hidden;
    background: var(--paper);
  }
  .letterhead {
    position: relative;
    width: 926px;
    height: 1200px;
    overflow: hidden;
    background: var(--paper);
    font-family: "Arimo", Arial, sans-serif;
    font-weight: 700;
  }
  .ridge-band {
    position: absolute;
    left: 0;
    top: 870px;
    width: 926px;
    height: 330px;
    background: linear-gradient(180deg, rgba(106, 179, 68, 0) 0%, var(--green-soft) 100%);
  }
  .tilted {
    position: absolute;
    margin: 0;
    transform-origin: 0 0;
    transform: rotate(45deg);
    white-space: nowrap;
    line-height: 1;
  }
  .brand {
    left: 38px;
    top: 940px;
    display: flex;
    align-items: center;
    gap: 12px;
  }
  .brand-square {
    width: 24px;
    height: 24px;
    background: var(--green);
  }
  .brand-name {
    font-size: 29px;
    letter-spacing: 0.5px;
    color: var(--charcoal);
    text-transform: uppercase;
  }
  .contact-line {
    font-size: 13.5px;
    color: var(--grey);
    text-transform: uppercase;
    letter-spacing: 0.2px;
  }
  .contact-title { left: 236px; top: 972px; }
  .contact-mail { left: 212px; top: 982px; }
  .contact-address { left: 190px; top: 992px; }
  .contact-name { color: var(--green); }
  .gap { display: inline-block; width: 16px; }
</style>
</head>
<body>
<main class="letterhead">
  <div class="ridge-band" role="img" aria-label="Green ridge line ornament running across the foot of the page"></div>

  <div class="tilted brand">
    <span class="brand-square"></span>
    <span class="brand-name">Dravesco Mining</span>
  </div>

  <p class="tilted contact-line contact-title">
    Managing Director <span class="contact-name">Tom Sealbrook</span>
  </p>
  <p class="tilted contact-line contact-mail">
    Tom@Dravesco.example<span class="gap"></span>555-314-2097
  </p>
  <p class="tilted contact-line contact-address">
    1186 Pelham #3 Dallas, TX 75209
  </p>
</main>
</body>
</html>
```